Real Estate Entrepreneur needs a business card

I am a real estate entrepreneur, I buy houses for investment purposes, I act as a real estate agent representing buyers and sellers in residential home transactions, I am a contractor that does a wide range of home repairs and construction. I'd like a design that can stick with me through the years as my business grows and morphs to fit any niche I decide to pursue as markets change.

Target Market(s)

Anyone with interest that may be related to real estate.

Industry/Entity Type

Real Estate

Contact Information for Business Card

A card that stands out and doesn't put me in any one box. My business will evolve over time and I need a card that can stay relevant.

Colors

Designer to choose colors to be used in the design.

Requirements
Must have
• Character
Nice to have
• I'm open
Should not have
• Cliche houses and hammers

```html
<!DOCTYPE html>
<html lang="en">
<head>
<meta charset="utf-8">
<title>Owen Hale — Business Card</title>
<link rel="stylesheet" href="https://fonts.googleapis.com/css2?family=Montserrat:wght@400;600&display=swap">
<style>
  :root {
    --backdrop: #e4e4e2;
    --card: #4a4745;
    --ink: #ffffff;
    --ink-soft: #e6e4e2;
  }
  html, body {
    margin: 0;
    padding: 0;
    width: 1200px;
    height: 801px;
    overflow: hidden;
    background: var(--backdrop);
    font-family: "Montserrat", sans-serif;
  }
  .stage {
    position: relative;
    width: 1200px;
    height: 801px;
  }
  .card {
    position: absolute;
    background: var(--card);
    color: var(--ink);
    border-radius: 2px;
    box-shadow: 0 6px 18px rgba(0, 0, 0, 0.18);
  }
  .card--front {
    left: 177px;
    top: 258px;
    width: 500px;
    height: 286px;
  }
  .card--back {
    left: 737px;
    top: 150px;
    width: 286px;
    height: 500px;
  }
  .identity {
    position: absolute;
    right: 262px;
    top: 150px;
    text-align: right;
  }
  .identity__name {
    font-weight: 600;
    font-size: 17px;
    letter-spacing: 0.3px;
    margin: 0;
  }
  .identity__role {
    font-weight: 400;
    font-size: 11px;
    letter-spacing: 0.6px;
    color: var(--ink-soft);
    margin: 2px 0 0;
  }
  .divider {
    position: absolute;
    left: 250px;
    top: 140px;
    width: 1px;
    height: 52px;
    background: var(--ink);
  }
  .contact {
    position: absolute;
    left: 266px;
    top: 144px;
    font-size: 11.5px;
    letter-spacing: 1px;
    line-height: 22px;
    color: var(--ink-soft);
  }
  .contact p { margin: 0; }
  .brand {
    position: absolute;
    left: 0;
    right: 0;
    top: 214px;
    text-align: center;
    font-weight: 400;
    font-size: 46px;
    letter-spacing: 2px;
    color: var(--ink);
  }
  .tagline {
    position: absolute;
    left: 18px;
    top: 290px;
    transform-origin: left top;
    transform: rotate(90deg) translateY(-100%);
    font-size: 15px;
    letter-spacing: 0.8px;
    color: var(--ink-soft);
    white-space: nowrap;
  }
</style>
</head>
<body>
  <main class="stage">
    <section class="card card--front" aria-label="Card front">
      <div class="identity">
        <p class="identity__name">Owen Hale</p>
        <p class="identity__role">Agent</p>
      </div>
      <div class="divider"></div>
      <div class="contact">
        <p>M : 99 48 512 07 36</p>
        <p>E : owen.h@hlvo.com</p>
      </div>
    </section>
    <section class="card card--back" aria-label="Card back">
      <div class="brand">Hale</div>
      <div class="tagline">Real Estate</div>
    </section>
  </main>
</body>
</html>
```